Laser Engraving Business Needs Shopify Front and Backend Site Design

We are starting up a brick laser engraving business and need the Shopify front and back end created. The design will stylistically match the logo we had designed and is attached (specifically the embossed shadowed logo). The ideal design will be dark themed.

The back end will support a standard product template with the ability to group products by type. The design will also include the ability to track visitor interaction with the site, as well as links to the companies social media accounts. Billing will be handled through Shopify and linked to company accounts.
Updates

Project has been guaranteed and 2nd place money added. Project requirements were adjusted slightly to reflect feedback that was sent out. Great submissions so far!

Industry/Entity Type

Business

Font styles to use
Sans Serif

Colors
ec1f27

Requirements
Must have
• The design will stylistically match the logo we had designed and is attached and be dark overall.
• Front end must include an About Us, Products, Social Media, Custom Design.
• The back end will support modular products grouped by type.
Nice to have
• A Placeholder page supporting photos, video and blog type content.

```html
<!DOCTYPE html>
<html lang="en">
<head>
<meta charset="utf-8">
<title>Brickline — Brick Wall Laser Engraving</title>
<link href="https://fonts.googleapis.com/css2?family=Montserrat:wght@400;500;600;700&family=Open+Sans:wght@400;600&display=swap" rel="stylesheet">
<style>
:root{
  --red:#e3202c;
  --yellow:#fbc92f;
  --dark:#2c2c2c;
  --darker:#1f1f1f;
  --darkest:#141414;
  --navy:#1f2632;
  --paper:#efefef;
  --ink:#2a2a2a;
  --muted:#8a8a8a;
  --light:#d8d8d8;
  --white:#ffffff;
}
*{margin:0;padding:0;box-sizing:border-box}
html,body{width:1200px;height:3212px;overflow:hidden}
body{font-family:"Open Sans",Arial,sans-serif;color:var(--ink);background:var(--paper);position:relative}
.h{font-family:"Montserrat",Arial,sans-serif}
section,header,footer,div,a,span,p{position:absolute}
a{text-decoration:none;color:inherit}

/* top bar */
.topbar{left:0;top:0;width:1200px;height:43px;background:#262626;color:#cfcfcf;font-size:12px}
.topbar span{top:14px}
.social-dot{width:12px;height:12px;border-radius:50%;background:#cfcfcf;top:16px}
.search{left:890px;top:6px;width:176px;height:30px;background:#1b1b1b;color:#bbb;font-size:12px;padding:7px 12px}

/* header */
.site-header{left:0;top:43px;width:1200px;height:114px;background:var(--dark)}
.brand{left:124px;top:24px;font-family:"Montserrat",Arial,sans-serif;font-weight:700;font-size:40px;color:var(--red);letter-spacing:1px}
.brand-mark{left:124px;top:30px;width:40px;height:40px;background:var(--red)}
.account{top:12px;font-size:12px;color:#d0d0d0}
.nav{top:58px;font-family:"Montserrat",Arial,sans-serif;font-size:13px;font-weight:600;color:#e0e0e0;letter-spacing:.5px}
.nav.active{color:var(--red)}

/* hero */
.hero{left:0;top:157px;width:1200px;height:509px}
.hero-photo{left:0;top:0;width:1200px;height:509px;background:linear-gradient(180deg,#c9ccd1 0%,#b9bcc2 55%,#7f8186 100%)}
.hero-kicker{left:0;width:1200px;top:154px;text-align:center;font-weight:700;font-size:23px;color:#1d1d1d;letter-spacing:1px}
.hero-title{left:0;width:1200px;top:180px;text-align:center;font-weight:700;font-size:70px;line-height:76px;color:#111;letter-spacing:3px}
.btn{display:block;text-align:center;font-family:"Montserrat",Arial,sans-serif;font-weight:700;color:var(--white);background:var(--red)}
.hero .btn{left:448px;top:364px;width:274px;height:53px;line-height:53px;font-size:19px;letter-spacing:1px}

/* features */
.features{left:0;top:666px;width:1200px;height:80px;background:#222}
.feature{top:0;width:316px;height:80px}
.feature.mid{background:#303030}
.feature-ico{left:44px;top:19px;width:42px;height:42px}
.feature-title{left:118px;top:22px;font-family:"Montserrat",Arial,sans-serif;font-weight:700;font-size:15px;color:var(--white)}
.feature-sub{left:118px;top:44px;font-size:11px;color:#bdbdbd}

/* section heading */
.sec-head{left:108px;width:950px;height:30px}
.sec-head::before,.sec-head::after{content:"";position:absolute;top:15px;width:270px;height:1px;background:#9a9a9a}
.sec-head::before{left:0}.sec-head::after{right:0}
.sec-head span{left:0;width:950px;text-align:center;font-family:"Montserrat",Arial,sans-serif;font-weight:600;font-size:23px;letter-spacing:2px;color:#222}

/* collections */
.collections{left:0;top:746px;width:1200px;height:536px;background:var(--paper)}
.tile{top:100px;width:302px;height:388px;border:6px solid #3a3a3a}
.tile-fill{left:0;top:0;width:100%;height:100%}
.tile-label{left:0;top:164px;width:100%;height:44px;line-height:44px;background:rgba(60,60,60,.85);text-align:center;color:var(--white);font-family:"Montserrat",Arial,sans-serif;font-weight:700;font-size:15px;letter-spacing:1px}

/* trending */
.trending{left:0;top:1282px;width:1200px;height:411px;background:linear-gradient(120deg,#222b38,#1a212c 60%,#252d3a)}
.trend-frame{left:129px;top:30px;width:557px;height:351px;background:#f0f0f0;padding:10px}
.trend-photo{left:10px;top:10px;width:537px;height:331px;background:linear-gradient(180deg,#8a5a40 0%,#6b4533 55%,#b9b6b0 80%,#d3d0ca 100%)}
.trend-title{left:709px;top:52px;color:var(--red);font-weight:700;font-size:24px;letter-spacing:1px}
.trend-text{left:709px;top:94px;width:300px;color:#dcdcdc;font-size:12.5px;line-height:19px}
.trend-price{left:709px;top:212px;color:#e0e0e0;font-size:13px}
.trend-price b{font-weight:400;color:var(--yellow);font-size:17px}
.trend .btn{top:282px;height:36px;line-height:36px;font-size:12px}
.btn.yellow{background:var(--yellow)}

/* featured */
.featured{left:0;top:1693px;width:1200px;height:671px;background:var(--paper)}
.card{top:129px;width:231px;height:210px}
.card-photo{left:0;top:0;width:231px;height:306px;border:4px solid #333}
.badge{left:0;top:0;height:22px;line-height:22px;padding:0 12px;background:var(--red);color:var(--white);font-family:"Montserrat",Arial,sans-serif;font-weight:700;font-size:11px}
.card-name{left:0;top:318px;font-size:12px;color:#333}
.card-type{left:0;top:344px;font-size:10px;color:#9a9a9a}
.card-price{left:0;top:366px;font-family:"Montserrat",Arial,sans-serif;font-weight:700;font-size:20px;color:#222}
.featured .more{left:489px;top:583px;width:192px;height:35px;line-height:35px;font-size:12px}

/* newsletter */
.newsletter{left:0;top:2364px;width:1200px;height:105px;background:var(--yellow)}
.nl-title{left:129px;top:32px;font-weight:600;font-size:19px;line-height:20px;color:#222;letter-spacing:1px}
.nl-text{left:306px;top:28px;width:272px;font-size:11.5px;line-height:17px;color:#333}
.nl-input{left:587px;top:40px;width:264px;height:32px;background:var(--white);font-size:11px;color:#555;padding:9px 10px}
.nl-btn{left:857px;top:40px;width:157px;height:32px;line-height:32px;background:#222;color:var(--white);text-align:center;font-family:"Montserrat",Arial,sans-serif;font-weight:700;font-size:12px}

/* testimonials */
.testimonials{left:0;top:2469px;width:1200px;height:420px;background:linear-gradient(125deg,#2f2f2f,#262626 50%,#333 100%)}
.t-title{left:0;width:1200px;top:38px;text-align:center;color:var(--white);font-weight:600;font-size:24px;letter-spacing:1px}
.avatar{left:516px;top:111px;width:138px;height:138px;border-radius:50%;border:5px solid #555;background:radial-gradient(circle at 50% 45%,#8aa2a8,#3e4d52)}
.t-text{left:270px;width:660px;top:290px;text-align:center;color:#e5e5e5;font-size:13px;line-height:22px}
.dot{top:368px;width:36px;height:4px;background:#cfcfcf}
.dot.on{background:var(--red)}

/* footer */
.site-footer{left:0;top:2889px;width:1200px;height:268px;background:#232323;color:#a8a8a8;font-size:11px}
.f-head{font-family:"Montserrat",Arial,sans-serif;font-weight:700;font-size:12px;color:var(--white);letter-spacing:.5px}
.f-text{line-height:16px}
.f-link{font-size:11px}
.pay{width:22px;height:14px;background:#8a8a8a;top:142px;border-radius:2px}
.bottom{left:0;top:3157px;width:1200px;height:55px;background:var(--darkest);color:#9a9a9a;font-size:11px}
</style>
</head>
<body>

<div class="topbar">
  <svg style="position:absolute;left:128px;top:15px" width="13" height="13" viewBox="0 0 24 24"><path d="M6 2h4l2 5-3 2a11 11 0 0 0 6 6l2-3 5 2v4a2 2 0 0 1-2 2A18 18 0 0 1 4 4a2 2 0 0 1 2-2z" fill="#cfcfcf"/></svg>
  <span style="left:146px">0100 555 0199</span>
  <svg style="position:absolute;left:246px;top:16px" width="14" height="11" viewBox="0 0 14 11"><rect x="0.5" y="0.5" width="13" height="10" fill="none" stroke="#cfcfcf"/><path d="M1 1l6 5 6-5" fill="none" stroke="#cfcfcf"/></svg>
  <span style="left:266px">info@brickline.com</span>
  <span style="left:402px;top:15px;width:20px;height:13px;background:#3c5a9a"></span>
  <span style="left:430px">USD ▾</span>
  <span class="social-dot" style="left:746px"></span>
  <span class="social-dot" style="left:766px"></span>
  <span class="social-dot" style="left:786px"></span>
  <span class="social-dot" style="left:806px"></span>
  <span class="social-dot" style="left:826px"></span>
  <div class="search">search our store
    <svg style="position:absolute;right:10px;top:9px" width="12" height="12" viewBox="0 0 12 12"><circle cx="5" cy="5" r="3.8" fill="none" stroke="#ddd" stroke-width="1.6"/><path d="M8 8l3 3" stroke="#ddd" stroke-width="1.6"/></svg>
  </div>
</div>

<header class="site-header">
  <span class="brand-mark"></span>
  <span class="brand" style="left:174px">BRICKLINE</span>
  <span class="account" style="left:742px">Login</span>
  <span class="account" style="left:782px">|</span>
  <span class="account" style="left:794px">Register</span>
  <span class="account" style="left:846px">|</span>
  <span class="account" style="left:862px">Shopping Cart / 0.00 Items</span>
  <svg style="position:absolute;left:1026px;top:8px" width="18" height="18" viewBox="0 0 18 18"><path d="M3 6h12l-1 11H4z" fill="#d0d0d0"/><path d="M6 6V4a3 3 0 0 1 6 0v2" fill="none" stroke="#d0d0d0" stroke-width="1.5"/></svg>
  <a class="nav active" style="left:524px">HOME</a>
  <a class="nav" style="left:597px">ABOUT US</a>
  <a class="nav" style="left:698px">PRODUCTS</a>
  <a class="nav" style="left:806px">NEWS</a>
  <a class="nav" style="left:876px">BLOG</a>
  <a class="nav" style="left:945px">CONTACT US</a>
</header>

<section class="hero">
  <div class="hero-photo" role="img" aria-label="Workspace with desks and lamps in front of a white laser-engraved brick wall"></div>
  <p class="hero-kicker h">LASER ENGRAVING TECHNOLOGY</p>
  <h1 class="hero-title h" style="position:absolute">BRICK WALL<br>LASER ENGRAVING</h1>
  <a class="btn">SHOP NOW</a>
</section>

<section class="features">
  <div class="feature" style="left:114px">
    <svg class="feature-ico" viewBox="0 0 42 42"><circle cx="21" cy="21" r="19" fill="none" stroke="#fff" stroke-width="2"/><text x="21" y="28" text-anchor="middle" font-family="Montserrat,sans-serif" font-size="18" fill="#fff">$</text></svg>
    <span class="feature-title">100% MONEY BACK</span><span class="feature-sub">GUARANTEE</span>
  </div>
  <div class="feature mid" style="left:428px">
    <svg class="feature-ico" viewBox="0 0 42 42"><circle cx="21" cy="21" r="19" fill="#fff"/><rect x="11" y="15" width="13" height="10" fill="#222"/><path d="M24 18h5l3 4v3h-8z" fill="#222"/><circle cx="15" cy="27" r="2" fill="#222"/><circle cx="28" cy="27" r="2" fill="#222"/></svg>
    <span class="feature-title">FREE SHIPPING</span><span class="feature-sub">ON ORDER OVER 500$</span>
  </div>
  <div class="feature" style="left:744px">
    <svg class="feature-ico" viewBox="0 0 42 42"><circle cx="21" cy="21" r="19" fill="none" stroke="#fff" stroke-width="2"/><circle cx="21" cy="21" r="9" fill="none" stroke="#fff" stroke-width="2"/><path d="M21 16v5h4" stroke="#fff" stroke-width="2" fill="none"/></svg>
    <span class="feature-title">24 HOUR</span><span class="feature-sub">ACTIVE SUPPORT</span>
  </div>
</section>

<section class="collections">
  <div class="sec-head" style="top:32px"><span>COLLECTIONS</span></div>
  <div class="tile" style="left:114px"><div class="tile-fill" role="img" aria-label="White herringbone brick pattern" style="background:linear-gradient(135deg,#f4f4f4,#e2e2e2)"></div><span class="tile-label">BRICK PATTERN - 1</span></div>
  <div class="tile" style="left:435px"><div class="tile-fill" role="img" aria-label="Grey stone brick pattern" style="background:linear-gradient(135deg,#a8a8a8,#8a8a8a)"></div><span class="tile-label">BRICK PATTERN - 2</span></div>
  <div class="tile" style="left:756px"><div class="tile-fill" role="img" aria-label="Flagstone pattern with dark joints" style="background:linear-gradient(135deg,#9aa3a6,#7f8a8c)"></div><span class="tile-label">BRICK PATTERN - 3</span></div>
</section>

<section class="trending trend">
  <div class="trend-frame"><div class="trend-photo" role="img" aria-label="Loft office with a red brick feature wall, desk and hanging lamps"></div></div>
  <h2 class="trend-title h" style="position:absolute">TRENDING BRICK WALL</h2>
  <p class="trend-text">Mauris sit amet tempus tortor. Curabitur eget magna quam. Cras bibendum scelerisque ullamcorper. Donec eget mauris imperdiet, consequat purus id, auctor enim. Nullam eleifend dapibus mattis. Interdum et malesuada fames ac ante ipsum primis in faucibus.</p>
  <p class="trend-price">Price: <b>500 $ /sq ft</b></p>
  <a class="btn yellow" style="left:709px;width:143px">MORE INFO</a>
  <a class="btn" style="left:861px;width:142px">BUY NOW</a>
</section>

<section class="featured">
  <div class="sec-head" style="top:58px"><span>FEATURED PRODUCTS</span></div>
  <div class="card" style="left:114px"><div class="card-photo" role="img" aria-label="White brick wall with pendant lamps over a dark wood floor" style="background:linear-gradient(180deg,#ececec 0%,#dcdcdc 68%,#3a3a3a 72%,#555 100%)"><span class="badge">NEW</span></div><span class="card-name">Lorem ipsum dolor sit amet</span><span class="card-type">Pattern Type : 235</span><span class="card-price">$ 256.00/sq ft.</span></div>
  <div class="card" style="left:351px"><div class="card-photo" role="img" aria-label="Office with red brick wall, desk and pendant lamps" style="background:linear-gradient(180deg,#8a5a40 0%,#6b4533 60%,#c9c6c0 78%,#d6d3cd 100%)"><span class="badge">NEW</span></div><span class="card-name">Lorem ipsum dolor sit amet</span><span class="card-type">Pattern Type : 235</span><span class="card-price">$ 256.00/sq ft.</span></div>
  <div class="card" style="left:589px"><div class="card-photo" role="img" aria-label="White brick wall with pendant lamps over a dark wood floor" style="background:linear-gradient(180deg,#ececec 0%,#dcdcdc 68%,#3a3a3a 72%,#555 100%)"><span class="badge">NEW</span></div><span class="card-name">Lorem ipsum dolor sit amet</span><span class="card-type">Pattern Type : 235</span><span class="card-price">$ 256.00/sq ft.</span></div>
  <div class="card" style="left:827px"><div class="card-photo" role="img" aria-label="White brick wall with pendant lamps over a dark wood floor" style="background:linear-gradient(180deg,#ececec 0%,#dcdcdc 68%,#3a3a3a 72%,#555 100%)"><span class="badge">NEW</span></div><span class="card-name">Lorem ipsum dolor sit amet</span><span class="card-type">Pattern Type : 235</span><span class="card-price">$ 256.00/sq ft.</span></div>
  <a class="btn more">MORE PRODUCT</a>
</section>

<section class="newsletter">
  <h3 class="nl-title h" style="position:absolute">SUBSCRIBE<br>NEWSLETTER</h3>
  <p class="nl-text">Lorem Ipsum dolor sit samwert est di maria nisi valeiex eist daan whckue monthey update , offeers and news and so m any.</p>
  <div class="nl-input">Enter your email id</div>
  <a class="nl-btn">SUBSCRIBE EMAIL</a>
</section>

<section class="testimonials">
  <h2 class="t-title h" style="position:absolute">WHAT CLIENTS SAYS ABOUT US</h2>
  <div class="avatar" role="img" aria-label="Client portrait"></div>
  <p class="t-text">Here are testimonials from clients that we have worked with and are happy to share their opinion about the process and the results. This is a testimonial straight from a client</p>
  <span class="dot on" style="left:472px"></span>
  <span class="dot" style="left:518px"></span>
  <span class="dot" style="left:564px"></span>
  <span class="dot" style="left:610px"></span>
  <span class="dot" style="left:656px"></span>
</section>

<footer class="site-footer">
  <span class="f-head" style="left:133px;top:22px">ABOUT BRICKLINE</span>
  <p class="f-text" style="left:133px;top:48px;width:300px">Lorem ipsum dolor sit amet lose potenti. Vesquam ante aliquet lacusemper elit. Cras neque nulla, convallis non commodo et, euismod nonsese.</p>
  <span class="f-head" style="left:133px;top:118px">WE CAN HELP YOU!</span>
  <p class="f-text" style="left:133px;top:150px;line-height:19px">Phone 1: 8 (400) 555—20—11<br>Phone 2: 8 (400) 555—65—26<br>Open - Close: 09:00-21:00<br>Mail: hello@brickline.com</p>

  <span class="f-head" style="left:516px;top:22px">SHOPPING</span>
  <span class="f-link" style="left:516px;top:61px">Your Cart</span>
  <span class="f-link" style="left:516px;top:93px">Your Orders</span>
  <span class="f-link" style="left:516px;top:125px">Addresses</span>
  <span class="f-link" style="left:516px;top:157px">Wishlist Items</span>
  <span class="f-link" style="left:516px;top:189px">Account</span>

  <span class="f-head" style="left:731px;top:22px">MORE LINK</span>
  <span class="f-link" style="left:731px;top:61px">Gift Center</span>
  <span class="f-link" style="left:731px;top:93px">Blog</span>
  <span class="f-link" style="left:731px;top:125px">Buying Guides</span>
  <span class="f-link" style="left:731px;top:157px">New Arrivals</span>
  <span class="f-link" style="left:731px;top:189px">Clearance</span>

  <span class="f-head" style="left:891px;top:22px">FOLLOW ME AND LIKE</span>
  <span style="left:891px;top:56px;width:13px;height:13px;border-radius:50%;background:#bdbdbd"></span>
  <span style="left:923px;top:56px;width:13px;height:13px;border-radius:50%;background:#bdbdbd"></span>
  <span style="left:955px;top:56px;width:13px;height:13px;border-radius:50%;background:#bdbdbd"></span>
  <span style="left:987px;top:56px;width:13px;height:13px;border-radius:50%;background:#bdbdbd"></span>
  <span class="f-head" style="left:891px;top:104px">PAYMENT ACCEPT</span>
  <span class="pay" style="left:891px"></span>
  <span class="pay" style="left:921px"></span>
  <span class="pay" style="left:951px"></span>
</footer>

<div class="bottom">
  <span style="left:131px;top:21px">Copyright 2017, Brickline</span>
  <span style="left:853px;top:21px">Returns</span>
  <span style="left:900px;top:21px">Sizing</span>
  <span style="left:940px;top:21px">International</span>
  <span style="left:1006px;top:21px">FAQs</span>
</div>

</body>
</html>
```